100% No Money Down

Flyer Design

Used for IG & FB (Social Media) Post. So avoid 8 1/2 x 11.

Target Market(s)

Real Estate Investors

Industry/Entity Type

Mortgage Brokerage

Requirements
Must have
• (LARGE BOLD FONT)
• 100% Investor Financing
• Fix & Flip Joint Ventures
• * Closing Costs Financed
• * 2-3 Week Close
• * No Score Minimum
• * No Reserve Requirement
• Contact: Marcus Delaney
• Bluekeel Financial Services, Inc.
• NMLS #58316 / #731840
• Direct (555) 482-0937
• Email mdelaney@bluekeelonline.example

```html
<!DOCTYPE html>
<html lang="en">
<head>
<meta charset="utf-8">
<title>100% No Money Down – Bluekeel Financial Services</title>
<link href="https://fonts.googleapis.com/css2?family=Montserrat:wght@500;600;700;800;900&display=swap" rel="stylesheet">
<style>
  :root{
    --page:#cfcfcf;
    --charcoal:#353535;
    --charcoal-panel:#3c3c3c;
    --gold:#dccb8f;
    --gold-soft:#cdbd85;
    --white:#ffffff;
    --photo-light:#eef0ee;
    --photo-mid:#d5dbd6;
    --photo-deep:#aebbb1;
  }
  *{box-sizing:border-box;margin:0;padding:0}
  html,body{width:1200px;height:1200px;overflow:hidden;background:var(--page);font-family:"Montserrat",sans-serif}
  .flyer{position:absolute;left:40px;top:101px;width:1120px;height:997px;overflow:hidden;background:var(--charcoal);box-shadow:0 4px 14px rgba(0,0,0,.25)}
  .hero-photo{position:absolute;left:0;top:0;width:1120px;height:560px;
    background:linear-gradient(160deg,var(--photo-light) 0%,var(--photo-mid) 45%,var(--photo-deep) 75%,var(--photo-mid) 100%)}
  .hero-panel{position:absolute;left:46px;top:0;width:355px;height:560px;background:rgba(255,255,255,.4)}
  .base{position:absolute;left:0;top:0}
  .brand{position:absolute;left:74px;top:140px;width:270px;display:flex;align-items:center;gap:12px;
    color:var(--charcoal);font-weight:800;font-size:19px;line-height:1.2;z-index:2}
  .brand-dot{flex:0 0 44px;height:44px;border-radius:50%;background:var(--gold-soft)}
  .circle{position:absolute;width:212px;height:212px;border-radius:50%;border:9px solid var(--white);
    box-shadow:0 3px 10px rgba(0,0,0,.35);z-index:3}
  .c1{left:121px;top:387px;background:linear-gradient(180deg,#5f7f9a 0%,#3f4c58 55%,#22262b 100%)}
  .c2{left:336px;top:354px;background:linear-gradient(180deg,#d9d2c4 0%,#a88a68 45%,#7a4a4a 75%,#5b5f75 100%)}
  .c3{left:556px;top:317px;background:linear-gradient(160deg,#f1f1ef 0%,#d6d2c9 50%,#a9b095 75%,#e8e6e0 100%)}
  .c4{left:758px;top:286px;background:linear-gradient(150deg,#f4efe5 0%,#cdb197 40%,#55526a 75%,#e9e1d3 100%)}
  .contact{position:absolute;left:65px;top:636px;width:330px;color:var(--white);z-index:2}
  .label{color:var(--gold);font-weight:800;font-size:21px;letter-spacing:.5px;text-transform:uppercase}
  .detail{font-weight:600;font-size:16px;line-height:23px;font-variant:small-caps;letter-spacing:.2px;white-space:nowrap}
  .detail.upper{text-transform:uppercase;font-size:14px}
  .group{margin-bottom:16px}
  .phone{display:flex;align-items:center;gap:14px;font-size:19px;font-weight:500;margin-top:22px}
  .offers{position:absolute;left:445px;top:636px;z-index:2}
  .headline{color:var(--gold);font-weight:900;font-size:41px;line-height:52px;letter-spacing:.6px;text-transform:uppercase;white-space:nowrap}
  .perks{list-style:none;margin-top:14px;color:var(--white);font-weight:700;font-size:27px;line-height:36px;font-variant:small-caps;letter-spacing:.8px}
</style>
</head>
<body>
  <main class="flyer">
    <div class="hero-photo" role="img" aria-label="Smiling man in a suit with dollar bills falling around him"></div>
    <div class="hero-panel"></div>
    <svg class="base" width="1120" height="997" viewBox="0 0 1120 997" aria-hidden="true">
      <polygon points="0,542 1120,377 1120,997 0,997" fill="var(--charcoal)"/>
      <polygon points="46,535 401,483 401,997 46,997" fill="var(--charcoal-panel)"/>
    </svg>

    <div class="brand"><span class="brand-dot"></span><span>Bluekeel Financial Services, Inc.</span></div>

    <div class="circle c1" role="img" aria-label="Portrait of loan officer Marcus Delaney"></div>
    <div class="circle c2" role="img" aria-label="Smiling contractor in a hard hat"></div>
    <div class="circle c3" role="img" aria-label="Kitchen renovation with cash in hand"></div>
    <div class="circle c4" role="img" aria-label="Investor reviewing paperwork with a calculator"></div>

    <section class="contact">
      <div class="group">
        <div class="label">Contact :</div>
        <div class="detail upper">Marcus Delaney</div>
        <div class="detail">Bluekeel Financial Services, Inc.</div>
        <div class="detail upper">NMLS #58316 / #731840</div>
      </div>
      <div class="group">
        <div class="label">Email</div>
        <div class="detail upper">mdelaney@bluekeelonline.example</div>
      </div>
      <div class="group">
        <div class="label">Website</div>
        <div class="detail upper">www.bluekeelonline.example</div>
      </div>
      <div class="phone">
        <svg width="14" height="24" viewBox="0 0 14 24" aria-hidden="true"><rect x="1" y="1" width="12" height="22" rx="2" fill="none" stroke="var(--gold)" stroke-width="2"/><circle cx="7" cy="19" r="1.4" fill="var(--gold)"/></svg>
        <span>(555) 482-0937 &nbsp;( Direct )</span>
      </div>
    </section>

    <section class="offers">
      <h1 class="headline">100% No Money Down</h1>
      <h2 class="headline">100% Investor Financing</h2>
      <h2 class="headline">Fix &amp; Flip Joint Ventures</h2>
      <ul class="perks">
        <li>Closing Costs Financed</li>
        <li>2-3 Week Close</li>
        <li>No Score Minimum</li>
        <li>No Reserve Requirement</li>
      </ul>
    </section>
  </main>
</body>
</html>
```